Business card design for a dynamic IT consulting company

We need a business card design for a young firm, specialized in the Telecommunications/Consulting industry. The name of the company is Brask and Partners Business Consulting Ltd. (Short name: Brask and Partnes)
Brask = solve read reverse, so we aim to be uncomplicated and solution-oriented. The small pipe in our logo is also related to the word solve. So we need a new business card design, which is simple, eye catching and something non traditional (I would probably prefer a square shaped design rather than a rectangle, but open for suggestions). Attached our logo.

Target Market(s)

Usually our customers are Tier1 Telecoms providers (Q-Linkra, Parnexo, etc) and their executives.

Industry/Entity Type

Business

Contact Information for Business Card

Name: Gergely Halmindo
Email: g.halmindo@braskpartnera.hu
Web: www.braskpartnera.hu
Mobile: +36 30 555 0192
Title: Managing Director

Optional:
Company name: Brask and Partners Ltd.
Address: 1047 Budapest, Ravaszi str. 17/B, Hungary

Font styles to use
Other font styles liked:
• helveticaneue_medium, Prime Regular are used now.

Colors

Designer to choose colors to be used in the design.

Requirements
Must have
• I would like to have a 2 sided design.
Nice to have
• I thought if we make the logo a bit bigger (without the company name), that could go to the back with the company name below. I though, if the pipe in the logo is somehow touchable on the business card, would be nice and unique.

```html
<!DOCTYPE html>
<html lang="en">
<head>
<meta charset="utf-8">
<title>Brask &amp; Partners – Business Card</title>
<link rel="stylesheet" href="https://fonts.googleapis.com/css2?family=Exo+2:wght@400;500&family=Work+Sans:wght@400;500&display=swap">
<style>
  :root {
    --backdrop: #1a1a1a;
    --card-white: #ffffff;
    --brand-blue: #139bd8;
    --accent-magenta: #b5178f;
    --ink-grey: #4a4a4a;
    --text-dark: #3c3c3c;
    --faint-circle: #f6f6f6;
  }
  * { margin: 0; padding: 0; box-sizing: border-box; }
  html, body {
    width: 1200px; height: 897px; overflow: hidden;
    background: var(--backdrop);
  }
  .stage { position: relative; width: 1200px; height: 897px; }
  .card {
    position: absolute; left: 303px; width: 595px; height: 338px;
    border-radius: 20px; overflow: hidden;
  }
  .card--front { top: 92px; background: var(--card-white); }
  .card--back { top: 469px; background: var(--brand-blue); }

  .front-decor { position: absolute; right: -40px; top: -20px; }

  .wordmark {
    position: absolute; display: flex; align-items: center;
    font-family: "Exo 2", sans-serif; font-weight: 400; white-space: nowrap;
  }
  .wordmark__square { display: block; background: currentColor; }
  .card--front .wordmark { left: 36px; top: 38px; color: var(--ink-grey); font-size: 38px; gap: 14px; }
  .card--front .wordmark__square { width: 16px; height: 16px; }
  .card--back .wordmark { left: 0; right: 0; top: 140px; justify-content: center; color: #fff; font-size: 54px; gap: 18px; }
  .card--back .wordmark__square { width: 22px; height: 22px; }

  .holder__name {
    position: absolute; left: 42px; top: 168px;
    font-family: "Exo 2", sans-serif; font-weight: 400; font-size: 22px;
    color: var(--brand-blue); letter-spacing: 0.5px;
  }
  .holder__title {
    position: absolute; left: 42px; top: 196px;
    font-family: "Work Sans", sans-serif; font-size: 14px; color: var(--text-dark);
  }
  .divider {
    position: absolute; left: 44px; right: 44px; top: 231px;
    height: 2px; background: var(--accent-magenta);
  }
  .contacts {
    position: absolute; left: 42px; top: 250px; list-style: none;
    font-family: "Work Sans", sans-serif; font-size: 13.5px; color: var(--text-dark);
  }
  .contacts li { display: flex; align-items: center; height: 19px; gap: 12px; }
  .contacts svg { width: 12px; height: 12px; fill: var(--brand-blue); flex: none; }
  .company {
    position: absolute; right: 44px; top: 254px; text-align: right;
    font-family: "Work Sans", sans-serif; font-size: 13.5px; color: var(--text-dark); line-height: 17px;
  }
  .company__name {
    font-family: "Exo 2", sans-serif; font-weight: 500; font-size: 15px;
    color: var(--brand-blue); margin-bottom: 2px;
  }
  .back__web {
    position: absolute; left: 0; right: 0; top: 296px; text-align: center;
    font-family: "Work Sans", sans-serif; font-size: 15px; letter-spacing: 2px; color: #fff;
  }
</style>
</head>
<body>
<main class="stage">
  <section class="card card--front">
    <svg class="front-decor" width="260" height="260" viewBox="0 0 260 260" aria-hidden="true">
      <circle cx="130" cy="130" r="125" fill="var(--faint-circle)"/>
    </svg>
    <div class="wordmark"><span class="wordmark__square"></span><span>Brask &amp; Partners</span></div>

    <h1 class="holder__name">GERGELY HALMINDO</h1>
    <p class="holder__title">Managing Director</p>
    <div class="divider"></div>

    <ul class="contacts">
      <li>
        <svg viewBox="0 0 24 24"><path d="M6.6 10.8a15.1 15.1 0 0 0 6.6 6.6l2.2-2.2a1 1 0 0 1 1-.25 11.4 11.4 0 0 0 3.6.57 1 1 0 0 1 1 1V20a1 1 0 0 1-1 1A17 17 0 0 1 3 4a1 1 0 0 1 1-1h3.5a1 1 0 0 1 1 1c0 1.25.2 2.45.57 3.57a1 1 0 0 1-.25 1z"/></svg>
        <span>+36 30 555 0192</span>
      </li>
      <li>
        <svg viewBox="0 0 24 24"><path d="M2 5h20v14H2z M2 5l10 8 10-8" fill="var(--brand-blue)"/><path d="M2 5l10 8 10-8" fill="none" stroke="#fff" stroke-width="2"/></svg>
        <span>g.halmindo@braskpartnera.hu</span>
      </li>
      <li>
        <svg viewBox="0 0 24 24"><circle cx="12" cy="12" r="10" fill="none" stroke="var(--brand-blue)" stroke-width="2"/><path d="M2 12h20M12 2c3 3 4 6.5 4 10s-1 7-4 10c-3-3-4-6.5-4-10s1-7 4-10z" fill="none" stroke="var(--brand-blue)" stroke-width="1.6"/></svg>
        <span>www.braskpartnera.hu</span>
      </li>
    </ul>

    <address class="company" style="font-style:normal">
      <div class="company__name">BRASK AND PARTNERS LTD.</div>
      <div>1047 Budapest, Ravaszi</div>
      <div>str. 17/B, Hungary</div>
    </address>
  </section>

  <section class="card card--back">
    <div class="wordmark"><span class="wordmark__square"></span><span>Brask &amp; Partners</span></div>
    <p class="back__web">www.braskpartnera.hu</p>
  </section>
</main>
</body>
</html>
```